Flyer-Design für Autolackiererei
Hallo es muss nur noch die Richtige Telefonnumer rein , die bekomm ich esrt von Fernova zu geschickt
Zielgruppe
Karosserie & Autolackiererei
Autohäuser , Privatkunden , Bussunterhemen , LKW Unterhemen , Versicherungen
Aufgabenstellung
Neueröffung Von Autolackiererei ab 01.03.2019 bitte ganz wichtig muss auf flayer drauf.
Unfallinstansetztung , Fahrzeuglackierung Jeglicher Art , Oldtimer Restauration , Fahrzeugaufbereitung , Achsvermessung ,Felgen Lackieren ,Hagelschaden ,
inspektionen alle Fahrzeug Fabrikaten, Mpk, Reifenservice
Hol und Bring service ,scheibenaustausch abwicklung mit versicherung ,
Smart Repair

```html
<!DOCTYPE html>
<html lang="de">
<head>
<meta charset="utf-8">
<title>Lackwerk Nord – Flyer</title>
<link rel="stylesheet" href="https://fonts.googleapis.com/css2?family=Oswald:wght@400;500&display=swap">
<style>
  :root {
    --paper: #f7f8fa;
    --ink: #3a3b40;
    --car-blue: #2357b5;
    --car-deep: #163d86;
    --car-light: #b9cdec;
    --brand-blue: #2aa7df;
  }
  * { margin: 0; padding: 0; box-sizing: border-box; }
  html, body { width: 1200px; height: 2396px; overflow: hidden; background: var(--paper); }
  .flyer {
    position: relative;
    width: 1200px;
    height: 2396px;
    overflow: hidden;
    background: var(--paper);
    font-family: "Oswald", "Arial Narrow", sans-serif;
    color: var(--ink);
  }
  .car-artwork {
    position: absolute;
    left: 0; top: 0;
    width: 1200px;
    height: 1900px;
    background:
      linear-gradient(to bottom, rgba(247,248,250,0) 72%, var(--paper) 100%),
      linear-gradient(100deg, var(--paper) 8%, #dfe5ee 22%, var(--car-light) 32%, var(--car-blue) 44%, var(--car-deep) 58%, var(--car-blue) 70%, var(--car-light) 86%, #eef2f7 100%);
  }
  .car-artwork::after {
    content: "";
    position: absolute;
    left: -300px; top: 1000px;
    width: 1100px; height: 1000px;
    background: radial-gradient(closest-side, var(--paper) 55%, rgba(247,248,250,0) 100%);
  }
  .brand {
    position: absolute;
    left: 160px;
    top: 1250px;
    display: flex;
    align-items: center;
    gap: 22px;
  }
  .brand-dot {
    width: 60px; height: 60px;
    border-radius: 50%;
    background: var(--brand-blue);
  }
  .brand-name {
    font-size: 44px;
    font-weight: 500;
    letter-spacing: 1px;
  }
  .address {
    position: absolute;
    left: 152px;
    top: 1555px;
    font-size: 34px;
    line-height: 54px;
    font-style: normal;
    text-transform: uppercase;
  }
  .phone {
    position: absolute;
    left: 152px;
    top: 1665px;
    font-size: 34px;
    line-height: 54px;
    text-transform: uppercase;
  }
  .opening {
    position: absolute;
    left: 152px;
    top: 1790px;
    font-size: 40px;
    line-height: 54px;
    font-weight: 500;
    color: var(--car-blue);
    text-transform: uppercase;
    letter-spacing: 1px;
  }
  .services {
    position: absolute;
    left: 148px;
    top: 1915px;
    width: 910px;
    font-size: 42px;
    line-height: 56px;
    text-transform: uppercase;
    letter-spacing: 1px;
  }
  .services-line {
    text-align: justify;
    text-align-last: justify;
    white-space: nowrap;
  }
</style>
</head>
<body>
<main class="flyer">
  <div class="car-artwork" role="img" aria-label="Skizzenhafte Illustration eines blauen Sportwagens in Frontansicht, weiß verwischter Hintergrund"></div>

  <div class="brand">
    <span class="brand-dot"></span>
    <span class="brand-name">Lackwerk Nord</span>
  </div>

  <address class="address">
    Lindenhofer Str. 12<br>
    21290 Heidekamp
  </address>

  <p class="phone">Tel.: 040 / 512 34 70</p>

  <p class="opening">Neueröffnung ab 01.03.2019</p>

  <section class="services">
    <div class="services-line">Unfallinstandsetztung | Fahrzeuglackierung</div>
    <div class="services-line">jeglicher Art | Oldtimer Restauration | Fahr-</div>
    <div class="services-line">zeugaufbereitung | Achsvermessung | Felgen</div>
    <div class="services-line">lackieren | Hagelschaden | Inspektionen für</div>
    <div class="services-line">alle Fahrzeugfabrikate | Mpk | Reifenservice</div>
    <div class="services-line">| Hol-und-Bring-Service | Scheibenaustausch |</div>
    <div class="services-line">Abwicklung mit Versicherung | Smart Repair</div>
  </section>
</main>
</body>
</html>
```